8.5 x 8.5 Tobin Marsh Flyer

Wednesday Workouts
with
Tobin Marsh
@liftwithtobinmarsh
Sponsored by ARBOR CREST HOMES GROUP
Join us Virtually each Wednesday from 7 - 7:30 pm
email frontdesk@arborcresthomes.example for Vidlo Link
reserved for ACHG Agents and Special Invitees
ARBOR CREST HOMES
Phone (555) 812-3367

```html
<!DOCTYPE html>
<html lang="en">
<head>
<meta charset="utf-8">
<title>Wednesday Workouts with Tobin Marsh</title>
<link rel="stylesheet" href="https://fonts.googleapis.com/css2?family=Roboto+Condensed:wght@300;400;500;700;900&display=swap">
<style>
:root{
  --teal:#0a9399;
  --teal-light:#14b3bb;
  --ink:#111111;
  --white:#ffffff;
  --paper-grey:#efefef;
  --photo-dark:#3b2f2b;
  --photo-mid:#6b5a50;
  --photo-haze:#c9c8c4;
}
*{margin:0;padding:0;box-sizing:border-box}
html,body{width:1200px;height:1200px;overflow:hidden;background:var(--white)}
.flyer{position:relative;width:1200px;height:1200px;overflow:hidden;background:var(--white);font-family:"Roboto Condensed",Arial,sans-serif;color:var(--ink)}
.hero-photo{position:absolute;inset:0;
  background:
    linear-gradient(90deg,var(--photo-dark) 0%,var(--photo-mid) 38%,var(--photo-haze) 62%,rgba(255,255,255,0) 86%);
}
.shapes{position:absolute;inset:0}
.brand-mark{position:absolute;left:800px;top:110px;width:340px;text-align:center;color:var(--teal);font-weight:700;font-size:46px;line-height:1.05;letter-spacing:1px}
.headline{position:absolute;color:var(--white);font-weight:900;text-transform:uppercase;line-height:1;text-shadow:2px 3px 4px rgba(0,0,0,.35);white-space:nowrap}
.headline--day{left:500px;top:308px;font-size:124px;letter-spacing:-1px}
.headline--workouts{left:612px;top:412px;font-size:124px;letter-spacing:-1px}
.host{position:absolute;left:530px;top:518px;color:var(--white);white-space:nowrap;font-size:92px;line-height:1}
.host .with{font-weight:300}
.host .name{font-weight:500}
.handle{position:absolute;left:624px;top:626px;display:flex;align-items:center;gap:18px;color:var(--white);font-size:32px;font-weight:400;letter-spacing:1px}
.details{position:absolute;right:228px;top:712px;text-align:right;white-space:nowrap}
.details .accent{color:var(--teal)}
.sponsor{font-size:26px;margin-bottom:20px}
.join{font-size:33px;line-height:1.22}
.join strong{color:var(--teal);font-weight:900}
.email{font-size:28px;line-height:1.3;margin-top:14px}
.reserved{font-size:25px;margin-top:14px}
.company{font-size:46px;font-weight:500;color:var(--teal);margin-top:18px;line-height:1.1}
.phone{display:flex;justify-content:flex-end;align-items:center;gap:16px;font-size:50px;font-weight:500;margin-top:8px;line-height:1}
.photo-circle{position:absolute;border-radius:50%;background:var(--white);padding:10px}
.photo-circle .ring{width:100%;height:100%;border-radius:50%;background:var(--ink);padding:9px}
.photo-circle .fill{width:100%;height:100%;border-radius:50%}
.circle-curls{left:90px;top:505px;width:394px;height:394px}
.circle-curls .fill{background:linear-gradient(160deg,#d9cbb8,#6d5c4f 60%,#3a3230)}
.circle-outdoor{left:-7px;top:810px;width:402px;height:402px}
.circle-outdoor .fill{background:linear-gradient(150deg,#6f8a4a,#a04060 55%,#7d7f84)}
.circle-squat{left:182px;top:702px;width:306px;height:306px}
.circle-squat .fill{background:linear-gradient(170deg,#8a8478,#3a3330 55%,#5e7f5a)}
.trainer-cutout{position:absolute;left:1006px;top:605px;width:194px;height:595px;border-radius:90px 90px 0 0;background:linear-gradient(180deg,#6a4a3a 0%,#3a2e2c 30%,#23252a 100%)}
.kettlebell{position:absolute;left:830px;top:1120px;width:160px;height:90px;border-radius:80px 80px 0 0;background:linear-gradient(180deg,#3a3a3a,#121212)}
</style>
</head>
<body>
<main class="flyer">
  <div class="hero-photo" role="img" aria-label="Photo of the trainer leaning forward during a gym workout"></div>

  <svg class="shapes" width="1200" height="1200" viewBox="0 0 1200 1200" aria-hidden="true">
    <polygon points="395,1029 840,1200 395,1200" fill="var(--paper-grey)"/>
    <polygon points="0,0 110,0 0,90" fill="var(--teal)"/>
    <polygon points="52,0 264,0 194,82 48,82" fill="var(--ink)"/>
    <polygon points="652,298 712,298 440,620 380,620" fill="var(--ink)"/>
    <polygon points="712,298 1200,298 1200,687 470,687 440,620" fill="var(--teal)"/>
    <polygon points="712,298 760,298 500,600 462,600" fill="var(--teal-light)"/>
    <polygon points="975,1200 1005,1160 1005,1200" fill="var(--teal)"/>
  </svg>

  <div class="brand-mark">ARBOR CREST<br>HOMES</div>

  <h1 class="headline headline--day">Wednesday</h1>
  <div class="headline headline--workouts">Workouts</div>
  <div class="host"><span class="with">with</span> <span class="name">Tobin Marsh</span></div>

  <div class="handle">
    <svg width="40" height="30" viewBox="0 0 40 30" aria-hidden="true">
      <rect x="1.5" y="1.5" width="37" height="27" fill="none" stroke="var(--white)" stroke-width="3"/>
      <polyline points="2,2 20,17 38,2" fill="none" stroke="var(--white)" stroke-width="3"/>
      <line x1="2" y1="28" x2="15" y2="13" stroke="var(--white)" stroke-width="3"/>
      <line x1="38" y1="28" x2="25" y2="13" stroke="var(--white)" stroke-width="3"/>
    </svg>
    <span>@liftwithtobinmarsh</span>
  </div>

  <div class="photo-circle circle-curls"><div class="ring"><div class="fill" role="img" aria-label="Photo of the trainer doing dumbbell curls indoors"></div></div></div>
  <div class="photo-circle circle-outdoor"><div class="ring"><div class="fill" role="img" aria-label="Photo of the trainer lifting dumbbells outdoors"></div></div></div>
  <div class="photo-circle circle-squat"><div class="ring"><div class="fill" role="img" aria-label="Photo of the trainer squatting over a medicine ball"></div></div></div>

  <div class="trainer-cutout" role="img" aria-label="Cut-out photo of the trainer standing in a tank top"></div>
  <div class="kettlebell" role="img" aria-label="Photo of a kettlebell"></div>

  <section class="details">
    <p class="sponsor">Sponsored by <span class="accent">ARBOR CREST HOMES GROUP</span></p>
    <p class="join">Join us Virtually each <strong>WEDNESDAY</strong><br>from <strong>7 - 7:30 pm</strong></p>
    <p class="email">Email <span class="accent">frontdesk@arborcresthomes.example</span><br>for Vidlo Link</p>
    <p class="reserved">Reserved for <span class="accent">ACHG Agents</span> and <span class="accent">Special Invitees</span></p>
    <p class="company">ARBOR CREST HOMES</p>
    <p class="phone">
      <svg width="34" height="34" viewBox="0 0 34 34" aria-hidden="true">
        <circle cx="17" cy="17" r="15" fill="none" stroke="var(--teal)" stroke-width="2.5"/>
        <path d="M12 9c-1.5 1-2.5 2.5-1.5 5 1.5 4 4.5 7.5 8.5 9.5 2.5 1 4 0 5-1.5l-3-3-2 1.2c-2-1-3.8-3-4.8-5l1.3-2z" fill="var(--teal)"/>
      </svg>
      <span>(555) 812-3367</span>
    </p>
  </section>
</main>
</body>
</html>
```